Business Card Design

After a corporate career in the finance sector I am now operating on my own as a consultant. I require a simple design, and want a strong card which is targeted at a conservative audience.

Target Market(s)

highly educated senior management, directors of companies, finance sector

Industry/Entity Type

Conservative

Contact Information for Business Card

Rosa Tindell
Consultant
Mobile: 0417 862 254
Email: rosa.tind@mailvora.com

Requirements
Should not have
• I don't want the colours green/yellow/brown

```html
<!DOCTYPE html>
<html lang="en">
<head>
<meta charset="utf-8">
<title>Rosa Tindell – Business Card</title>
<link rel="stylesheet" href="https://fonts.googleapis.com/css2?family=Noto+Sans:wght@400;700&display=swap">
<style>
  :root {
    --backdrop: #d3d4d6;
    --card-white: #ffffff;
    --ink-black: #000000;
    --accent-blue: #0a74be;
    --text-white: #ffffff;
  }
  * { margin: 0; padding: 0; box-sizing: border-box; }
  html, body {
    width: 1200px;
    height: 1200px;
    overflow: hidden;
    background: var(--backdrop);
    font-family: "Noto Sans", Verdana, sans-serif;
  }
  .card {
    position: absolute;
    left: 136px;
    top: 320px;
    width: 928px;
    height: 560px;
    background: var(--card-white);
    overflow: hidden;
  }
  .identity {
    position: absolute;
    left: 75px;
    top: 80px;
  }
  .identity__name {
    font-weight: 700;
    font-size: 58px;
    line-height: 62px;
    color: var(--ink-black);
    letter-spacing: 1px;
  }
  .identity__title {
    font-weight: 400;
    font-size: 41px;
    line-height: 44px;
    color: var(--accent-blue);
  }
  .rule-accent {
    position: absolute;
    left: 0;
    top: 275px;
    width: 523px;
    height: 8px;
    background: var(--accent-blue);
  }
  .rule-thin {
    position: absolute;
    left: 0;
    top: 290px;
    width: 100%;
    height: 10px;
    background: var(--ink-black);
  }
  .contact-band {
    position: absolute;
    left: 0;
    top: 307px;
    width: 100%;
    height: 253px;
    background: var(--ink-black);
  }
  .contact-list {
    position: absolute;
    left: 502px;
    top: 108px;
    list-style: none;
  }
  .contact-list__item {
    display: flex;
    align-items: center;
    height: 45px;
    color: var(--text-white);
    font-size: 31px;
    letter-spacing: 0.5px;
  }
  .contact-list__icon {
    width: 29px;
    height: 29px;
    margin-right: 16px;
    flex: none;
  }
</style>
</head>
<body>
  <main class="card">
    <header class="identity">
      <h1 class="identity__name">Rosa Tindell</h1>
      <p class="identity__title">Consultant</p>
    </header>

    <div class="rule-accent"></div>
    <div class="rule-thin"></div>

    <section class="contact-band">
      <ul class="contact-list">
        <li class="contact-list__item">
          <svg class="contact-list__icon" viewBox="0 0 29 29" aria-hidden="true">
            <circle cx="14.5" cy="14.5" r="14.5" fill="var(--text-white)"/>
            <rect x="10" y="6" width="9" height="17" rx="1.5" fill="var(--accent-blue)"/>
            <rect x="11.5" y="8" width="6" height="5" fill="var(--text-white)"/>
            <g fill="var(--text-white)">
              <rect x="11.5" y="15" width="1.6" height="1.4"/>
              <rect x="13.7" y="15" width="1.6" height="1.4"/>
              <rect x="15.9" y="15" width="1.6" height="1.4"/>
              <rect x="11.5" y="17.4" width="1.6" height="1.4"/>
              <rect x="13.7" y="17.4" width="1.6" height="1.4"/>
              <rect x="15.9" y="17.4" width="1.6" height="1.4"/>
              <rect x="11.5" y="19.8" width="1.6" height="1.4"/>
              <rect x="13.7" y="19.8" width="1.6" height="1.4"/>
              <rect x="15.9" y="19.8" width="1.6" height="1.4"/>
            </g>
          </svg>
          <span class="contact-list__text">0417 862 254</span>
        </li>
        <li class="contact-list__item">
          <svg class="contact-list__icon" viewBox="0 0 29 29" aria-hidden="true">
            <circle cx="14.5" cy="14.5" r="14.5" fill="var(--text-white)"/>
            <rect x="5.5" y="9" width="18" height="12" fill="var(--accent-blue)"/>
            <path d="M6.5 10 L14.5 16 L22.5 10 M6.5 20 L12 15 M22.5 20 L17 15" fill="none" stroke="var(--text-white)" stroke-width="1.3"/>
          </svg>
          <span class="contact-list__text">rosa.tind@mailvora.com</span>
        </li>
      </ul>
    </section>
  </main>
</body>
</html>
```